Letterhead to coordinate with business card

I am needing a docx template and print file for a letterhead to co-ordinate with my newly designed logo and business card.

```html
<!DOCTYPE html>
<html lang="en">
<head>
<meta charset="utf-8">
<title>Harbour Plan Services – Letterhead</title>
<link rel="stylesheet" href="https://fonts.googleapis.com/css2?family=Arimo:wght@400&display=swap">
<style>
  :root {
    --backdrop: #d9dadc;
    --paper: #f4f4f5;
    --ink: #1c1c1e;
    --berry: #9b2c60;
    --teal: #0f7a78;
    --mark-faint: rgba(15, 122, 120, 0.07);
  }
  * { margin: 0; padding: 0; box-sizing: border-box; }
  html, body {
    width: 1200px;
    height: 1141px;
    overflow: hidden;
    background: var(--backdrop);
    font-family: "Arimo", Arial, sans-serif;
  }
  .letterhead {
    position: absolute;
    left: 333px;
    top: 87px;
    width: 675px;
    height: 948px;
    background: var(--paper);
    box-shadow: 2px 3px 6px rgba(0, 0, 0, 0.22);
  }
  .brand {
    position: absolute;
    left: 40px;
    top: 48px;
    width: 150px;
    display: flex;
    flex-direction: column;
    align-items: center;
  }
  .brand-square {
    width: 52px;
    height: 52px;
    background: var(--berry);
  }
  .brand-name {
    margin-top: 10px;
    font-size: 13px;
    font-weight: 400;
    color: var(--teal);
    white-space: nowrap;
  }
  .contact {
    position: absolute;
    left: 412px;
    top: 52px;
    font-size: 11.2px;
    line-height: 14px;
    color: var(--ink);
    list-style: none;
  }
  .contact li {
    display: flex;
    align-items: flex-start;
  }
  .contact .gap { margin-top: 5px; }
  .contact svg {
    width: 9px;
    height: 9px;
    margin: 2.5px 5px 0 0;
    flex: none;
    fill: var(--teal);
  }
  .faint-mark {
    position: absolute;
    left: 165px;
    top: 349px;
    width: 346px;
    height: 346px;
    background: var(--mark-faint);
  }
</style>
</head>
<body>
  <main class="letterhead">
    <header class="brand">
      <div class="brand-square"></div>
      <div class="brand-name">Harbour Plan Services</div>
    </header>

    <ul class="contact">
      <li>
        <svg viewBox="0 0 10 10" aria-hidden="true"><path d="M5 0a3.5 3.5 0 0 0-3.5 3.5C1.5 6 5 10 5 10s3.5-4 3.5-6.5A3.5 3.5 0 0 0 5 0zm0 4.8a1.3 1.3 0 1 1 0-2.6 1.3 1.3 0 0 1 0 2.6z"/></svg>
        <span>Harbour Plan Services<br>PO Box 482<br>Lakeside NSW 2405</span>
      </li>
      <li class="gap">
        <svg viewBox="0 0 10 10" aria-hidden="true"><path d="M2 0.5l1.6 2.2-1 1.1c.6 1.3 1.5 2.2 2.7 2.8l1.1-1 2.1 1.6-.9 1.8C4.6 8.8 1 5.3.7 1.4z"/></svg>
        <span>0400 318 964</span>
      </li>
      <li>
        <svg viewBox="0 0 10 10" aria-hidden="true"><path d="M0.5 2h9v6h-9z M1 2.5l4 3 4-3" stroke="#f4f4f5" stroke-width="0.8"/></svg>
        <span>hello@harbourplanservices.com.au</span>
      </li>
      <li>
        <svg viewBox="0 0 10 10" aria-hidden="true"><circle cx="5" cy="5" r="4.2" fill="none" stroke="#0f7a78" stroke-width="0.9"/><path d="M0.8 5h8.4M5 0.8c-2.2 2.5-2.2 5.9 0 8.4M5 0.8c2.2 2.5 2.2 5.9 0 8.4" fill="none" stroke="#0f7a78" stroke-width="0.7"/></svg>
        <span>harbourplanservices.com.au</span>
      </li>
    </ul>

    <div class="faint-mark" aria-hidden="true"></div>
  </main>
</body>
</html>
```